Renewable Energy company needs a new website

We are renewable energy company that has been operating for 3 years now and require a new website design. We are looking to upgrade our website to be comparable to our competitors. We are not a brick and mortar business so our website does need to be very appealing and convey a sense of authenticity and trust to the consumer. It will also heavily display our current system special and offering etc. The final design needs to be visually appealing in a marketing sense however also needs to convey a high sense of professionalism.

Target Market(s)

Consumers of solar systems for installation on their home or business.

Coding

Coded - Design and coding required

Number of Pages Required

3 page

Font styles to use
Sans Serif

Colors

Designer to choose colors to be used in the design.

Requirements
Must have
• A home page, a page for residential solar systems including the packages we are currently offering and a commercial page for larger installations of solar systems.
• www.pelvantpower.com.au
Nice to have
• As a template we do like this https://www.marowindsun.com.au/qld/ in terms of design elements and layout of the page.

```html
<!DOCTYPE html>
<html lang="en">
<head>
<meta charset="utf-8">
<title>Tolvane Energy – Engineering and Economic Solutions</title>
<link rel="stylesheet" href="https://fonts.googleapis.com/css2?family=Cinzel:wght@600;700&family=Roboto:wght@400;500;700&display=swap">
<style>
:root{
  --red:#b5121b;
  --red-dark:#8f0d14;
  --navy:#232a3e;
  --navy-deep:#1b2030;
  --ink:#1f2330;
  --muted:#6b6f7a;
  --pale:#e4e8f4;
  --white:#ffffff;
  --line:#e2e2e2;
}
*{box-sizing:border-box;margin:0;padding:0}
html,body{width:1200px;height:4246px;overflow:hidden;background:var(--white)}
body{font-family:'Roboto',sans-serif;color:var(--ink);position:relative}
.serif{font-family:'Cinzel',serif;font-weight:700;letter-spacing:.5px}
section,header,footer{position:relative;width:1200px;overflow:hidden}

/* header */
.site-header{height:127px;background:var(--white)}
.callbar{position:absolute;right:0;top:0;width:445px;height:44px;background:var(--red);clip-path:polygon(8% 0,100% 0,100% 100%,0 100%);color:var(--white);font-weight:700;font-size:20px;display:flex;align-items:center;padding-left:62px;gap:8px}
.brand{position:absolute;left:120px;top:24px}
.brand-name{display:block;font-size:32px;font-weight:700;color:var(--red);line-height:32px}
.brand-tag{position:absolute;left:120px;top:93px;font-size:10.5px;color:var(--ink);letter-spacing:.2px}
.main-nav{position:absolute;left:394px;top:78px;display:flex;gap:34px;font-size:16px;font-weight:700;color:var(--navy)}
.main-nav .active{color:var(--red);border-bottom:3px solid var(--red);padding-bottom:10px}

/* hero */
.hero{height:557px;background:linear-gradient(180deg,#dfe6f0 0%,#b8cbe2 45%,#5a7fb6 68%,#1d3f8c 82%,#10307a 100%)}
.hero-card{position:absolute;left:135px;top:153px;width:404px;height:239px;background:var(--white);box-shadow:0 4px 16px rgba(0,0,0,.18);text-align:center;padding-top:30px}
.hero-card h1{font-size:27px;line-height:35px;color:var(--ink)}
.btn-red{display:inline-block;background:var(--red);color:var(--white);font-weight:700;font-size:17px;padding:13px 32px;margin-top:22px}

/* features */
.features{height:424px}
.feature{position:absolute;width:230px;text-align:center}
.feature-ring{width:132px;height:132px;border:6px solid var(--red);border-radius:50%;margin:0 auto;display:flex;align-items:center;justify-content:center}
.feature h3{font-size:20px;line-height:23px;margin-top:17px;color:var(--navy)}
.feature p{font-size:13px;line-height:18px;color:var(--muted);margin-top:12px}

/* splits */
.split{height:463px;display:flex}
.split .photo{width:600px;height:100%}
.split .copy{width:600px;height:100%;padding:72px 0 0 79px}
.split h2{font-size:29px;line-height:37px}
.split p{font-size:14px;line-height:23px;margin-top:20px;max-width:420px}
.btn-outline{display:inline-block;border:3px solid var(--red);color:var(--red);font-weight:700;font-size:17px;padding:13px 33px;margin-top:24px}
.split-one .copy{background:var(--pale);color:var(--ink)}
.split-two{height:461px}
.split-two .copy{background:var(--navy);color:var(--white);padding:100px 0 0 135px}
.split-two .btn-outline{border-color:var(--white);color:var(--white)}

/* why */
.why{height:758px;background:var(--white)}
.why h2{position:absolute;top:62px;width:100%;text-align:center;font-size:29px}
.why .ring{position:absolute;left:437px;top:118px;width:330px;height:330px;border-radius:50%;border:7px solid #dadada}
.why .hub{position:absolute;left:478px;top:159px;width:248px;height:248px;border-radius:50%;background:var(--white);box-shadow:0 0 28px rgba(0,0,0,.1)}
.dot{position:absolute;width:30px;height:30px;border-radius:50%;background:var(--white);border:3px solid #d4d4d4;transform:translate(-50%,-50%)}
.dot::after{content:"";position:absolute;left:6px;top:6px;width:12px;height:12px;border-radius:50%;background:var(--navy)}
.why-icon{position:absolute;width:86px;height:86px;border-radius:50%;transform:translate(-50%,-50%);display:flex;align-items:center;justify-content:center}
.why-icon.navy{background:var(--navy)}
.why-icon.red{background:var(--red)}
.why-item{position:absolute;width:260px}
.why-item h3{font-size:17px;line-height:21px;color:var(--ink)}
.why-item p{font-size:12.5px;line-height:16px;color:var(--muted);margin-top:5px}
.why-item.right{text-align:right}
.why-item.center{text-align:center;width:320px}

/* testimonials */
.testimonials{height:445px;background:linear-gradient(180deg,#eef0f4 0%,#dfe3ea 60%,#cdd3dc 100%)}
.testimonials h2{position:absolute;top:74px;width:100%;text-align:center;font-size:29px}
.quote-card{position:absolute;top:147px;width:417px;height:207px;background:var(--white);border:3px solid #e6e6e6;text-align:center;padding:38px 30px 0}
.quote-card p{font-size:19px;line-height:27px;color:#4a4d55}
.quote-card .who{font-size:18px;margin-top:18px;color:var(--ink)}
.quote-card .role{font-size:13px;color:var(--muted)}
.arrow{position:absolute;top:216px}

/* partners */
.partners{height:303px}
.partners h2{position:absolute;top:66px;width:100%;text-align:center;font-size:29px}
.badge{position:absolute;background:#d7d9de}

/* quote & contact */
.enquiry{height:526px;display:flex}
.enquiry .quote{width:590px;height:100%;background:linear-gradient(180deg,#c8141e 0%,#b1121a 55%,#8e0f15 100%);padding:68px 0 0 143px;color:var(--white)}
.enquiry .contact{width:610px;height:100%;background:linear-gradient(180deg,#2a3145 0%,#232a3e 100%);padding:84px 0 0 71px;color:var(--white)}
.enquiry h2{font-size:26px;line-height:30px}
.field{width:402px;height:43px;border:1px solid rgba(255,255,255,.7);background:rgba(255,255,255,.08);margin-top:12px;font-size:15px;padding:12px 20px}
.field.first{margin-top:20px}
.field.msg{height:102px}
.btn-white{display:inline-block;border:3px solid var(--white);font-weight:700;font-size:17px;padding:13px 33px;margin:17px 0 0 5px}
.contact-list{margin-top:28px}
.contact-row{display:flex;gap:22px;font-size:16px;line-height:25px;margin-bottom:24px;align-items:flex-start}
.contact-row svg{flex:none;margin-top:6px}

/* footer */
.site-footer{height:182px;background:var(--navy-deep);text-align:center;color:var(--white)}
.foot-nav{display:flex;justify-content:center;gap:30px;font-size:15px;font-weight:700;padding-top:46px}
.copy-line{font-size:13px;color:#a8acb8;margin-top:14px}
.social{display:flex;justify-content:center;gap:8px;margin-top:20px}
.social span{width:37px;height:37px;border-radius:50%;border:2px solid var(--white)}
</style>
</head>
<body>

<header class="site-header">
  <div class="callbar">
    <svg width="20" height="20" viewBox="0 0 24 24" fill="#fff"><path d="M6.6 10.8a15 15 0 0 0 6.6 6.6l2.2-2.2c.3-.3.7-.4 1-.2 1.1.4 2.3.6 3.6.6.6 0 1 .4 1 1V20c0 .6-.4 1-1 1A17 17 0 0 1 3 4c0-.6.4-1 1-1h3.5c.6 0 1 .4 1 1 0 1.3.2 2.5.6 3.6.1.3 0 .7-.2 1z"/></svg>
    CALL US: (07) 3000 4812
  </div>
  <div class="brand"><span class="brand-name">TOLVANE<br>ENERGY</span></div>
  <div class="brand-tag">ENGINEERING AND ECONOMIC SOLUTIONS</div>
  <nav class="main-nav">
    <span class="active">HOME</span><span>ABOUT US</span><span>RESIDENTIAL</span><span>COMMERCIAL</span><span>OFF-GRID</span><span>FREE QUOTE</span>
  </nav>
</header>

<section class="hero" role="img" aria-label="Solar panel field in front of wind turbines on hills under a bright sky">
  <div class="hero-card">
    <h1 class="serif">TIRED OF THE POWER<br>BILL GETTING<br>LARGER EACH YEAR?</h1>
    <span class="btn-red">GET A QUOTE</span>
  </div>
</section>

<section class="features">
  <div class="feature" style="left:99px;top:63px">
    <div class="feature-ring"><svg width="60" height="60" viewBox="0 0 60 60" fill="none" stroke="#1f2330" stroke-width="2.5"><path d="M8 8v44h44"/><path d="M18 50V30M28 50V36M38 50V42"/><path d="M14 14l34 30M48 34v10H38"/></svg></div>
    <h3>Reduce Costs, Grow<br>Your Business</h3>
    <p>If you're running a business, then our Commercial Energy Solutions are perfectly suited</p>
  </div>
  <div class="feature" style="left:358px;top:63px">
    <div class="feature-ring"><svg width="60" height="60" viewBox="0 0 60 60" fill="none" stroke="#1f2330" stroke-width="2.5"><circle cx="30" cy="30" r="14"/><path d="M32 20l-6 11h8l-6 10"/><path d="M30 4v7M30 49v7M4 30h7M49 30h7M12 12l5 5M43 43l5 5M48 12l-5 5M17 43l-5 5"/></svg></div>
    <h3>Avoid Blackouts,<br>Go Off-Grid</h3>
    <p>If you're running a business, then our Commercial In a country where blackouts</p>
  </div>
  <div class="feature" style="left:615px;top:63px">
    <div class="feature-ring"><svg width="64" height="60" viewBox="0 0 64 60" fill="none" stroke="#1f2330" stroke-width="2.5"><circle cx="32" cy="12" r="5"/><path d="M32 2v3M24 12h-3M43 12h-3"/><path d="M14 24h36l6 16H8z"/><path d="M26 24l-3 16M38 24l3 16M11 32h42"/><path d="M32 40v12M22 54h20"/></svg></div>
    <h3>Go Solar, Eliminate<br>Fuel Cost</h3>
    <p>We know you want to grow so we help you find more cost-efficient alternatives versus</p>
  </div>
  <div class="feature" style="left:874px;top:63px">
    <div class="feature-ring"><svg width="64" height="60" viewBox="0 0 64 60" fill="none" stroke="#1f2330" stroke-width="2.5"><circle cx="34" cy="14" r="9"/><path d="M12 34c0-8 8-14 20-14s20 6 20 14c0 5-3 9-7 11v7h-7v-5h-12v5h-7v-7c-4-2-7-5-7-11z"/><path d="M52 32h5"/></svg></div>
    <h3>Save Money For<br>Your Family</h3>
    <p>Our Residential Solar Power solutions can give you up to 80% reduction on your power bills</p>
  </div>
</section>

<section class="split split-one">
  <div class="photo" role="img" aria-label="Rows of solar panels stretching towards a city skyline at sunset" style="background:linear-gradient(180deg,#cfe0ef 0%,#e9e4d2 35%,#4d6f9a 60%,#1f3a66 100%)"></div>
  <div class="copy">
    <h2 class="serif">BRIGHTMILL CUT 80% OFF<br>THEIR POWER BILL</h2>
    <p>Whether you're a huge commercial establishment or a small property owner, Tolvane Energy has the perfect solution to give you consistent savings on your monthly bills.</p>
    <p>Get your FREE Quote and discover how you can save thousands of dollars from reduced energy cost by choosing to go solar!</p>
    <span class="btn-outline">LEARN MORE</span>
  </div>
</section>

<section class="split split-two">
  <div class="copy">
    <h2 class="serif">PLUG INTO THE SUN</h2>
    <p>At Tolvane Energy, we believe that you deserve better. Poor services and huge costs for electricity don't sit well with us. That's why we do our best to provide our clients with up-to-date energy management systems that can immediately result to significant reductions in their electricity expenses.</p>
    <span class="btn-outline">LEARN MORE</span>
  </div>
  <div class="photo" role="img" aria-label="Light bulb resting in soil beside a green seedling" style="background:radial-gradient(circle at 65% 45%,#f4f4ee 0%,#c7d88a 18%,#5f8a2a 45%,#2f4a17 75%,#3a2a1c 100%)"></div>
</section>

<section class="why">
  <h2 class="serif">WHY DO YOU NEED TO GO SOLAR?</h2>
  <div class="ring"></div>
  <div class="hub"></div>
  <span class="dot" style="left:470px;top:180px"></span>
  <span class="dot" style="left:729px;top:180px"></span>
  <span class="dot" style="left:460px;top:389px"></span>
  <span class="dot" style="left:739px;top:389px"></span>
  <span class="dot" style="left:602px;top:461px"></span>

  <div class="why-icon navy" style="left:376px;top:198px"><svg width="40" height="40" viewBox="0 0 40 40" fill="none" stroke="#fff" stroke-width="2"><circle cx="22" cy="14" r="7"/><path d="M22 10v8M20 12h4"/><path d="M4 30h6l8 4h12l6-6"/></svg></div>
  <div class="why-item right" style="left:136px;top:242px;width:260px"><h3>Get Consistent Savings<br>for 20+ Years</h3><p>We can't deny that the cost of electricity is consistently rising. And whether you're a commercial</p></div>

  <div class="why-icon navy" style="left:822px;top:193px"><svg width="40" height="40" viewBox="0 0 40 40" fill="none" stroke="#fff" stroke-width="2.2"><path d="M20 36V22L10 8M20 22l10-14M6 10l4-2 1 5M34 10l-4-2-1 5"/></svg></div>
  <div class="why-item" style="left:799px;top:242px;width:270px"><h3>Differentiate Your<br>Business Against Competitors</h3><p>With the increasing awareness of people with regards to global warming, being an organisation</p></div>

  <div class="why-icon red" style="left:381px;top:432px"><svg width="42" height="42" viewBox="0 0 42 42" fill="none" stroke="#fff" stroke-width="2.4"><path d="M14 10a14 14 0 1 0 14 0"/><path d="M21 5v16"/></svg></div>
  <div class="why-item right" style="left:162px;top:478px;width:260px"><h3>Be Independent<br>from The Grid</h3><p>Gone are the days when the only way to use electricity</p></div>

  <div class="why-icon red" style="left:822px;top:432px"><svg width="42" height="42" viewBox="0 0 42 42" fill="none" stroke="#fff" stroke-width="2"><circle cx="21" cy="21" r="15"/><path d="M8 16c5 0 7 4 11 3s3-7 8-8M14 34c2-5 8-5 9-10s7-2 11 0"/></svg></div>
  <div class="why-item" style="left:788px;top:478px;width:260px"><h3>Take Part in Solving<br>Global Warming</h3><p>Solar energy is clean, renewable and sustainable. Unlike using fossil fuels, solar energy</p></div>

  <div class="why-icon navy" style="left:602px;top:544px"><svg width="42" height="42" viewBox="0 0 42 42" fill="none" stroke="#fff" stroke-width="2"><path d="M8 34V26M15 34V22M22 34V18M29 34V14M36 34V10M4 36h36M8 20l10-8 6 4 10-8"/></svg></div>
  <div class="why-item center" style="left:442px;top:593px"><h3>Increase and Maximise<br>Your Bottomline</h3><p>Saving money on electricity costs is only half of the equation. The money you save</p></div>
</section>

<section class="testimonials" role="img" aria-label="Faded offshore wind turbines over the sea">
  <h2 class="serif">WHAT OUR CLIENTS ARE SAYING</h2>
  <svg class="arrow" style="left:106px" width="28" height="56" viewBox="0 0 28 56" fill="none" stroke="#4a4d55" stroke-width="2.5"><path d="M26 2L2 28l24 26"/></svg>
  <div class="quote-card" style="left:166px">
    <p>My new solar water pump hasn't missed a beat and have saved me a fortune in diesel fuel</p>
    <div class="who">DARREN</div><div class="role">Client</div>
  </div>
  <div class="quote-card" style="left:616px">
    <p>Have been a pleasure to deal with and came up with a combinations of ideas to save money</p>
    <div class="who">LUCILLE</div><div class="role">Client</div>
  </div>
  <svg class="arrow" style="left:1072px" width="28" height="56" viewBox="0 0 28 56" fill="none" stroke="#4a4d55" stroke-width="2.5"><path d="M2 2l24 26L2 54"/></svg>
</section>

<section class="partners">
  <h2 class="serif">OUR PARTNERS</h2>
  <span class="badge" style="left:140px;width:136px;top:168px;height:36px"></span>
  <span class="badge" style="left:355px;width:118px;border-radius:50%;height:72px;top:150px"></span>
  <span class="badge" style="left:527px;width:152px;top:168px;height:40px"></span>
  <span class="badge" style="left:738px;width:154px;top:166px;height:44px"></span>
  <span class="badge" style="left:966px;width:96px;top:156px;height:62px"></span>
</section>

<section class="enquiry">
  <div class="quote" role="img" aria-label="Red toned field of solar panels">
    <h2 class="serif">FREE NO<br>OBLIGATION QUOTE!</h2>
    <div class="field first">Name</div>
    <div class="field">Email address</div>
    <div class="field">Phone Number</div>
    <div class="field msg">Message</div>
    <span class="btn-white">SUBMIT NOW</span>
  </div>
  <div class="contact">
    <h2 class="serif">CONTACT US</h2>
    <div class="contact-list">
      <div class="contact-row"><svg width="36" height="36" viewBox="0 0 24 24" fill="none" stroke="#fff" stroke-width="1.2"><path d="M6.6 10.8a15 15 0 0 0 6.6 6.6l2.2-2.2c.3-.3.7-.4 1-.2 1.1.4 2.3.6 3.6.6.6 0 1 .4 1 1V20c0 .6-.4 1-1 1A17 17 0 0 1 3 4c0-.6.4-1 1-1h3.5c.6 0 1 .4 1 1 0 1.3.2 2.5.6 3.6.1.3 0 .7-.2 1z"/></svg><div>Phone<br>(07) 3000 4812</div></div>
      <div class="contact-row"><svg width="36" height="36" viewBox="0 0 24 24" fill="none" stroke="#fff" stroke-width="1.2"><path d="M12 22s7-7 7-12a7 7 0 0 0-14 0c0 5 7 12 7 12z"/><circle cx="12" cy="10" r="2.5"/></svg><div>Address<br>118-126 Harlow Lane<br>Ridgeview QLD 4000</div></div>
      <div class="contact-row"><svg width="36" height="36" viewBox="0 0 24 24" fill="none" stroke="#fff" stroke-width="1.2"><rect x="3" y="5" width="18" height="14"/><path d="M3 5l9 8 9-8M3 19l7-7M21 19l-7-7"/></svg><div>Email address<br>info@tolvaneenergy.com.au</div></div>
      <div class="contact-row"><svg width="36" height="36" viewBox="0 0 24 24" fill="none" stroke="#fff" stroke-width="1.2"><circle cx="12" cy="12" r="9"/><circle cx="12" cy="12" r="6"/><path d="M12 8v4l3 2"/></svg><div>Working Hours<br>Mon to Fri: 9:00AM - 5:00PM</div></div>
    </div>
  </div>
</section>

<footer class="site-footer">
  <nav class="foot-nav"><span>HOME</span><span>ABOUT US</span><span>RESIDENTIAL</span><span>COMMERCIAL</span><span>OFF-GRID</span><span>FREE QUOTE</span></nav>
  <div class="copy-line">© 2019 Company Name. All right reserved</div>
  <div class="social" aria-label="Social links"><span></span><span></span><span></span></div>
</footer>

</body>
</html>
```